"Use it or Lose it" and "Brush on Over"

We are a dental office looking to connect with our patients through direct mail advertising. With the last 3 months of the year coming we would like to send out Post Cards to our patients letting them know they have 3 months left to "USE IT OR LOSE IT" when it comes to their dental insurance benefits.
So we are looking for a post card that has the "Use It or Lost it" theme along with our dental office logo, telephone number and address.

We are also looking for a post card that says "Brush On Over" to remind our patients that they are due for a dental cleaning and we would like for them to come over to our dental office for a well needed cleaning :).

```html
<!DOCTYPE html>
<html lang="en">
<head>
<meta charset="utf-8">
<title>Kestrel Dental Postcards</title>
<link href="https://fonts.googleapis.com/css2?family=Catamaran:wght@500;600;700;800&display=swap" rel="stylesheet">
<style>
  :root {
    --board: #dcdcdc;
    --navy: #232a55;
    --white: #ffffff;
    --green: #8dc63f;
    --yellow: #f5c400;
    --brand: #2f6bb5;
    --label: #3a4058;
    --clock-face: #f4f4f4;
    --clock-notes: #9aa58f;
    --clock-rim: #2b2b2b;
  }
  * { box-sizing: border-box; margin: 0; padding: 0; }
  html, body { width: 1200px; height: 902px; overflow: hidden; }
  body {
    background: var(--board);
    font-family: "Catamaran", sans-serif;
    position: relative;
  }
  .card {
    position: absolute;
    width: 527px;
    height: 379px;
    background: var(--navy);
    overflow: hidden;
    color: var(--white);
  }
  .card__shape { position: absolute; inset: 0; width: 527px; height: 379px; }
  .card-label {
    position: absolute;
    width: 527px;
    text-align: center;
    font-weight: 700;
    font-size: 17px;
    color: var(--label);
  }

  .brand {
    position: absolute;
    display: flex;
    align-items: center;
    gap: 6px;
    font-weight: 700;
    font-size: 22px;
    line-height: 1;
    color: var(--brand);
    white-space: nowrap;
  }
  .brand__dot { width: 16px; height: 16px; border-radius: 50%; background: var(--brand); }

  .headline { position: absolute; left: 66px; font-weight: 800; line-height: 1; }
  .headline > div { display: block; }
  .hl-use { font-size: 70px; height: 52px; letter-spacing: -2px; }
  .hl-mid { height: 50px; }
  .hl-it { font-size: 52px; letter-spacing: -1px; margin-right: 6px; }
  .hl-or { font-size: 72px; color: var(--green); letter-spacing: -2px; }
  .hl-lose { font-size: 42px; height: 42px; letter-spacing: -1px; }
  .hl-lose .hl-it { font-size: 58px; margin-left: 4px; margin-right: 0; }

  .brush { position: absolute; left: 66px; font-weight: 800; line-height: 1; }
  .brush__top { font-size: 60px; height: 48px; letter-spacing: -1px; }
  .brush__bottom { font-size: 44px; color: var(--green); letter-spacing: -1.5px; }

  .tagline { position: absolute; left: 66px; font-size: 8.5px; font-weight: 600; line-height: 10.5px; }
  .tagline .hl-green { color: var(--green); }
  .tagline .hl-yellow { color: var(--yellow); }

  .divider { position: absolute; left: 66px; width: 70px; height: 1px; background: var(--white); }
  .body-copy { position: absolute; left: 66px; width: 108px; font-size: 8.5px; font-weight: 600; line-height: 10.1px; }

  .calendar { position: absolute; left: 66px; width: 54px; }
  .calendar svg { display: block; }
  .calendar__caption { font-size: 9px; font-weight: 600; margin-top: 1px; }

  .contact {
    position: absolute;
    top: 331px;
    left: 195px;
    display: flex;
    align-items: center;
    gap: 10px;
    font-size: 12px;
    font-weight: 600;
    color: var(--navy);
    white-space: nowrap;
  }
  .contact__item { display: flex; align-items: center; gap: 4px; }

  .media--clock {
    position: absolute;
    left: 301px;
    top: 174px;
    width: 144px;
    height: 144px;
    border-radius: 50%;
    background: radial-gradient(circle, var(--clock-face) 0 35%, var(--clock-notes) 80%);
    border: 7px solid var(--clock-rim);
  }
  .media--family { position: absolute; inset: 0; width: 527px; height: 379px; }

  .stamp { position: absolute; left: 427px; top: 36px; width: 64px; height: 56px; border: 1.5px dashed #777; padding: 4px; }
  .stamp__inner { width: 100%; height: 100%; border: 1px solid #777; }
  .address { position: absolute; left: 327px; top: 164px; color: var(--navy); font-size: 10px; font-weight: 700; }
  .address__line { position: absolute; left: 327px; width: 159px; height: 1px; background: #333; }
</style>
</head>
<body>

<!-- Card 01 front -->
<section class="card card--front" style="left:53px;top:50px">
  <svg class="card__shape" viewBox="0 0 527 379" aria-hidden="true">
    <path d="M424,0 C300,70 190,250 131,379 L527,379 L527,0 Z" fill="#fff"/>
    <circle cx="318" cy="88" r="44" fill="#fff"/>
  </svg>
  <div class="brand" style="left:290px;top:76px"><span class="brand__dot"></span>Kestrel Dental</div>
  <div class="headline" style="top:52px">
    <div class="hl-use">Use</div>
    <div class="hl-mid"><span class="hl-it">it</span><span class="hl-or">or</span></div>
    <div class="hl-lose">Lose<span class="hl-it">it!</span></div>
  </div>
  <p class="tagline" style="top:210px">Don't Let Your<br><span class="hl-green">Dental Insurance Benefits</span><br><span class="hl-yellow">Go to Waste!</span></p>
  <div class="calendar" style="top:260px">
    <svg width="52" height="56" viewBox="0 0 52 56" aria-hidden="true">
      <rect x="1" y="6" width="50" height="49" fill="none" stroke="#fff" stroke-width="2"/>
      <line x1="1" y1="20" x2="51" y2="20" stroke="#fff" stroke-width="1.5"/>
      <g fill="none" stroke="#fff" stroke-width="2"><circle cx="12" cy="5" r="3.5"/><circle cx="21" cy="5" r="3.5"/><circle cx="31" cy="5" r="3.5"/><circle cx="40" cy="5" r="3.5"/></g>
      <text x="26" y="17" font-family="Catamaran, sans-serif" font-size="8" font-weight="700" fill="#fff" text-anchor="middle">December</text>
      <text x="22" y="47" font-family="Catamaran, sans-serif" font-size="24" font-weight="800" fill="#fff" text-anchor="middle">31</text>
      <text x="38" y="33" font-family="Catamaran, sans-serif" font-size="9" font-weight="700" fill="#fff">st</text>
    </svg>
    <div class="calendar__caption">Expiring on</div>
  </div>
  <div class="media--clock" role="img" aria-label="Photo of an alarm clock filled with dollar bills"></div>
  <div class="contact">
    <span class="contact__item"><svg width="10" height="10" viewBox="0 0 10 10" aria-hidden="true"><circle cx="5" cy="5" r="5" fill="#232a55"/><path d="M3 2.5 L4 2.5 L4.6 4 L4 4.5 Q4.6 5.6 5.5 6 L6 5.4 L7.5 6 L7.5 7 Q5 7.5 3 4.5 Z" fill="#fff"/></svg>555 - 014 - 2290</span>
    <span class="contact__item"><svg width="10" height="10" viewBox="0 0 10 10" aria-hidden="true"><circle cx="5" cy="5" r="5" fill="#232a55"/><circle cx="5" cy="5" r="2" fill="none" stroke="#fff" stroke-width="1.2"/></svg>www.KestrelDental.com</span>
  </div>
</section>
<div class="card-label" style="left:53px;top:437px">Card 01 Front</div>

<!-- Card 01 back -->
<section class="card card--back" style="left:621px;top:50px">
  <svg class="card__shape" viewBox="0 0 527 379" aria-hidden="true">
    <path d="M319,0 C260,90 210,230 194,379 L527,379 L527,0 Z" fill="#fff"/>
  </svg>
  <div class="brand" style="left:62px;top:46px"><span class="brand__dot"></span>Kestrel Dental</div>
  <div class="headline" style="top:80px">
    <div class="hl-use">Use</div>
    <div class="hl-mid"><span class="hl-it">it</span><span class="hl-or">or</span></div>
    <div class="hl-lose">Lose<span class="hl-it">it!</span></div>
  </div>
  <p class="tagline" style="top:234px">Don't Let Your<br><span class="hl-green">Dental Insurance Benefits</span><br><span class="hl-yellow">Go to Waste!</span></p>
  <div class="calendar" style="top:272px">
    <svg width="44" height="48" viewBox="0 0 52 56" aria-hidden="true">
      <rect x="1" y="6" width="50" height="49" fill="none" stroke="#fff" stroke-width="2"/>
      <line x1="1" y1="20" x2="51" y2="20" stroke="#fff" stroke-width="1.5"/>
      <g fill="none" stroke="#fff" stroke-width="2"><circle cx="12" cy="5" r="3.5"/><circle cx="21" cy="5" r="3.5"/><circle cx="31" cy="5" r="3.5"/><circle cx="40" cy="5" r="3.5"/></g>
      <text x="26" y="17" font-family="Catamaran, sans-serif" font-size="8" font-weight="700" fill="#fff" text-anchor="middle">December</text>
      <text x="22" y="47" font-family="Catamaran, sans-serif" font-size="24" font-weight="800" fill="#fff" text-anchor="middle">31</text>
      <text x="38" y="33" font-family="Catamaran, sans-serif" font-size="9" font-weight="700" fill="#fff">st</text>
    </svg>
    <div class="calendar__caption">Expiring on</div>
  </div>
  <div class="stamp"><div class="stamp__inner"></div></div>
  <div class="address">TO:</div>
  <div class="address__line" style="top:200px"></div>
  <div class="address__line" style="top:228px"></div>
  <div class="address__line" style="top:256px"></div>
  <div class="contact">
    <span class="contact__item"><svg width="10" height="10" viewBox="0 0 10 10" aria-hidden="true"><circle cx="5" cy="5" r="5" fill="#232a55"/><path d="M3 2.5 L4 2.5 L4.6 4 L4 4.5 Q4.6 5.6 5.5 6 L6 5.4 L7.5 6 L7.5 7 Q5 7.5 3 4.5 Z" fill="#fff"/></svg>555 - 014 - 2290</span>
    <span class="contact__item"><svg width="10" height="10" viewBox="0 0 10 10" aria-hidden="true"><circle cx="5" cy="5" r="5" fill="#232a55"/><circle cx="5" cy="5" r="2" fill="none" stroke="#fff" stroke-width="1.2"/></svg>www.KestrelDental.com</span>
  </div>
</section>
<div class="card-label" style="left:621px;top:437px">Card 01 Back</div>

<!-- Card 02 front -->
<section class="card card--front" style="left:53px;top:474px">
  <svg class="card__shape" viewBox="0 0 527 379" aria-hidden="true">
    <path d="M424,0 C300,70 190,250 131,379 L527,379 L527,0 Z" fill="#fff"/>
    <circle cx="318" cy="88" r="44" fill="#fff"/>
  </svg>
  <svg class="media--family" viewBox="0 0 527 379" role="img" aria-label="Photo of a smiling family of four">
    <defs>
      <clipPath id="family-clip"><path d="M424,0 C300,70 190,250 131,379 L527,379 L527,0 Z"/></clipPath>
      <radialGradient id="family-tone" cx="0.6" cy="0.45" r="0.6">
        <stop offset="0" stop-color="#e9d6c6"/>
        <stop offset="0.55" stop-color="#c9a58c"/>
        <stop offset="1" stop-color="#f2f2f2"/>
      </radialGradient>
    </defs>
    <rect x="179" y="142" width="348" height="237" fill="url(#family-tone)" clip-path="url(#family-clip)"/>
  </svg>
  <div class="brand" style="left:290px;top:76px"><span class="brand__dot"></span>Kestrel Dental</div>
  <div class="brush" style="top:52px">
    <div class="brush__top">Brush</div>
    <div class="brush__bottom">On Over</div>
  </div>
  <p class="tagline" style="top:160px">Don't Let Your<br><span class="hl-green">Dental Insurance Benefits</span><br><span class="hl-yellow">Go to Waste!</span></p>
  <div class="divider" style="top:198px"></div>
  <p class="body-copy" style="top:206px">Your teeth are important. You use them to eat, and your smile gives people their first impression of you. For such an important part of you, you'll want only top-quality experts to help keep them in the best shape possible.</p>
  <div class="contact">
    <span class="contact__item"><svg width="10" height="10" viewBox="0 0 10 10" aria-hidden="true"><circle cx="5" cy="5" r="5" fill="#232a55"/><path d="M3 2.5 L4 2.5 L4.6 4 L4 4.5 Q4.6 5.6 5.5 6 L6 5.4 L7.5 6 L7.5 7 Q5 7.5 3 4.5 Z" fill="#fff"/></svg>555 - 014 - 2290</span>
    <span class="contact__item"><svg width="10" height="10" viewBox="0 0 10 10" aria-hidden="true"><circle cx="5" cy="5" r="5" fill="#232a55"/><circle cx="5" cy="5" r="2" fill="none" stroke="#fff" stroke-width="1.2"/></svg>www.KestrelDental.com</span>
  </div>
</section>
<div class="card-label" style="left:53px;top:862px">Card 02 Front</div>

<!-- Card 02 back -->
<section class="card card--back" style="left:621px;top:474px">
  <svg class="card__shape" viewBox="0 0 527 379" aria-hidden="true">
    <path d="M319,0 C260,90 210,230 194,379 L527,379 L527,0 Z" fill="#fff"/>
  </svg>
  <div class="brand" style="left:62px;top:50px"><span class="brand__dot"></span>Kestrel Dental</div>
  <div class="brush" style="top:82px">
    <div class="brush__top">Brush</div>
    <div class="brush__bottom">On Over</div>
  </div>
  <p class="tagline" style="top:166px">Don't Let Your<br><span class="hl-green">Dental Insurance Benefits</span><br><span class="hl-yellow">Go to Waste!</span></p>
  <div class="divider" style="top:206px"></div>
  <p class="body-copy" style="top:214px">Your teeth are important. You use them to eat, and your smile gives people their first impression of you. For such an important part of you, you'll want only top-quality experts to help keep them in the best shape possible.</p>
  <div class="stamp"><div class="stamp__inner"></div></div>
  <div class="address">TO:</div>
  <div class="address__line" style="top:200px"></div>
  <div class="address__line" style="top:228px"></div>
  <div class="address__line" style="top:256px"></div>
  <div class="contact">
    <span class="contact__item"><svg width="10" height="10" viewBox="0 0 10 10" aria-hidden="true"><circle cx="5" cy="5" r="5" fill="#232a55"/><path d="M3 2.5 L4 2.5 L4.6 4 L4 4.5 Q4.6 5.6 5.5 6 L6 5.4 L7.5 6 L7.5 7 Q5 7.5 3 4.5 Z" fill="#fff"/></svg>555 - 014 - 2290</span>
    <span class="contact__item"><svg width="10" height="10" viewBox="0 0 10 10" aria-hidden="true"><circle cx="5" cy="5" r="5" fill="#232a55"/><circle cx="5" cy="5" r="2" fill="none" stroke="#fff" stroke-width="1.2"/></svg>www.KestrelDental.com</span>
  </div>
</section>
<div class="card-label" style="left:621px;top:862px">Card 02 Back</div>

</body>
</html>
```